Food Package Design (Soybean Rice Nuggets)

We Need package design for our new item. Here's detail:

BAG DIMENSION:
62/4 X 10 1/2 X 3 1/2 INCH
STAND UP BAG (ATTACHED PIC)
ARTWORK TEMPLATE ATTACHED (Please erase the contents in the attached template. Use the teamplte only).
At the end of the project, I will need printable, editable file with print die line

<Front side package>
The Crispy Crunchy Soybean Rice Nuggets
Belvri TM logo on top (*FILE UPLOADED)

Gluten Free
No Trans Fat
No Cholesterol
Net Weight 5 oz (142g)

<Back Side>
Soft and chewy rice puffs covered with roasted soybean powders. Belvri’s Soybean Rice Nuggets hit the other end of the spectrum. These are light, crunchy, crispy and savory and make a delicious that you might not be able to stop eating.

Ingredients: rice powder, palm oil, soybean powder, salt, sugar, corn grits

Contains soybean

Manufactured exclusively for Belvri (logo)
Tarrowfield, CA 90000
Made in Korea

www.belvrisnacks.example

Nutrition Facts (*File uploaded)
Serving Size 30g
Seriving Per Container About 5
Calories 140
Calories from Fat 45
Total Fat 5g 8%
Saturated Fat 2.5g 13%
Trans Fat 0g
Cholesterol 0mg 0%
Sodium 30mg 1%
Total Carbohydrate 22g 7%
Dietary Fiber 0g 0%
Sugars 4g
Protein 2g

Vitamin A 0%
Vitamin C 0%
Calcium 0%
Iron 0%

Barcode (*FILE UPLOADED)

* If I find a design I like, I could end my project earlier than deadline. I prefer to end the project sooner than deadline!
*If you need any images to purchase, please let me know.
Thank you for your participation and interest in our project!

Target Market(s)

HEALTH CONSCIOUS CONSUMERS, CONSUMER WHO LOVE SNACKING AND ALWAYS LOOKING FOR INNOVATIVE, UNIQUE, HEALTHY SNACKS.

Requirements
Must have
• FUN, BOLDNESS, MODERN, PLAYFUL, EYE CATCHING DESIGN

```html
<!DOCTYPE html>
<html lang="en">
<head>
<meta charset="utf-8">
<title>Belvri Soybean Rice Nuggets – Front Panel</title>
<link rel="stylesheet" href="https://fonts.googleapis.com/css2?family=Kaushan+Script&family=Yellowtail&family=Lato:wght@400;700&display=swap">
<style>
  :root {
    --artboard: #3a3a3c;
    --panel: #fbe096;
    --panel-low: #f7dc98;
    --trim: #e5007e;
    --brand-red: #e41e26;
    --ink: #111111;
    --snack-gold: #e6a14d;
    --plate-dark: #3d3a31;
  }
  * { margin: 0; padding: 0; box-sizing: border-box; }
  html, body {
    width: 839px; height: 1200px; overflow: hidden;
    background: var(--artboard);
  }
  .canvas { position: relative; width: 839px; height: 1200px; }

  .front-panel {
    position: absolute; left: 52px; top: 86px;
    width: 735px; height: 1027px;
    background: linear-gradient(var(--panel) 0%, var(--panel) 50%, var(--panel-low) 100%);
    outline: 1px solid var(--trim);
    overflow: hidden;
  }

  .brand-tab {
    position: absolute; left: 270px; top: 0;
    width: 193px; height: 168px;
    background: var(--brand-red);
    border-radius: 0 0 26px 26px;
    display: flex; align-items: center; justify-content: center;
  }
  .brand-name {
    font-family: "Lato", sans-serif; font-weight: 700;
    font-size: 44px; color: #ffffff; letter-spacing: 1px;
  }

  .product-title { position: absolute; left: 0; top: 0; width: 100%; }
  .title-lead {
    position: absolute; left: 214px; top: 222px;
    font-family: "Kaushan Script", cursive;
    font-size: 50px; color: var(--ink); white-space: nowrap;
  }
  .title-main {
    position: absolute; font-family: "Yellowtail", cursive;
    color: var(--brand-red); white-space: nowrap; line-height: 1;
  }
  .title-main.line-one { left: 118px; top: 292px; font-size: 100px; }
  .title-main.line-two { left: 265px; top: 370px; font-size: 100px; }

  .claims {
    position: absolute; left: 49px; top: 490px;
    font-family: "Lato", sans-serif; color: var(--ink);
  }
  .claim-lead { font-size: 32px; font-weight: 700; line-height: 1; }
  .claim { margin-top: 18px; font-size: 34px; font-weight: 700; line-height: 1; }
  .claim small { font-size: 17px; font-weight: 400; margin-left: 4px; }
  .claim + .claim { margin-top: 14px; }

  .product-photo {
    position: absolute; left: 15px; top: 472px;
    width: 705px; height: 520px;
    background: radial-gradient(ellipse 42% 44% at 50% 52%,
      var(--snack-gold) 0%, #d9913f 60%, var(--plate-dark) 80%,
      #8a7a5c 90%, rgba(247,220,152,0) 100%);
  }

  .net-weight {
    position: absolute; right: 50px; top: 945px;
    font-family: "Lato", sans-serif; font-weight: 700;
    font-size: 25px; color: var(--ink);
  }
</style>
</head>
<body>
<main class="canvas">
  <section class="front-panel">
    <div class="brand-tab"><span class="brand-name">Belvri</span></div>

    <h1 class="product-title">
      <span class="title-lead">The Crispy Crunchy</span>
      <span class="title-main line-one">Soybean Rice</span>
      <span class="title-main line-two">Nuggets</span>
    </h1>

    <div class="product-photo" role="img" aria-label="Golden soybean rice nuggets piled on a square speckled stoneware plate"></div>

    <ul class="claims" style="list-style:none">
      <li class="claim-lead">Gluten Free</li>
      <li class="claim">No <small>Trans Fat</small></li>
      <li class="claim">No <small>Cholesterol</small></li>
    </ul>

    <p class="net-weight">Net Weight 5 oz (142g)</p>
  </section>
</main>
</body>
</html>
```